Willowmere Spa and Beauty Ltd. (Name of business)

I need a business card designed for this new company based out of Toronto Ontario. We specialize in Eyelash Extensions, Manicures and Pedicures, body waxing, massages, laser hair removal and botox treatments. Also offer a variety of products for sale, such as skin cream serums, collagen gel, eye cream, etc. It is a safe relaxing and non-judgemental environnment. Clients are welcome to come be pampered for the half or full day. Many service packages to choose from.

Open 7days per week from 8am to 8pm.

Marissa Thornbury
Spa Facilitator
Willowmere Spa and Beauty Ltd.
7200 Calder Ave; Suite 1400
Toronto ON K8P 2W7

OFFICE: 416.739.4100
FAX: 416.739.4101
CELL: 416.582.6074
EMAIL: marissa.thornbury@willowmerespa.example

Target Market(s)

Target market is primarily female ranging from 16 years old to 50 years old.

Industry/Entity Type

Business

Contact Information for Business Card

Marissa Thornbury
Spa Facilitator
7200 Calder Ave; Suite 1400
Toronto ON K8P 2W7

OFFICE: 416.739.4100
FAX: 416.739.4101
CELL: 416.582.6074

Logo Text

I dont have a logo yet. I would like it simple but sophisticated and modern.

Font styles to use
Serif

Requirements
Must have
• all pertinent details such as company name, logo, name and contact information, services that are offered, including package rates
Nice to have
• Company name and logo prominent. A card that is neat and the information such as address, phone number, fax, email, etc is not too crowded but laid out in an easy to read format.
• Possibly on the back of card - some of the services offered could be listed, as well as professional cream lotions and serums. Hours of operation etc.

```html
<!DOCTYPE html>
<html lang="en">
<head>
<meta charset="utf-8">
<title>Willowmere Spa and Beauty – Business Card</title>
<link rel="stylesheet" href="https://fonts.googleapis.com/css2?family=Arimo:wght@400;700&family=Italianno&display=swap">
<style>
  :root {
    --card-bg: #a67a79;
    --card-border: #4a4a4a;
    --text-peach: #f7d4c3;
    --script-mauve: #cf9a98;
    --mark-pink: #f5a9ad;
  }
  html, body {
    margin: 0;
    padding: 0;
    width: 1200px;
    height: 680px;
    overflow: hidden;
    background: #ffffff;
  }
  .card {
    position: relative;
    box-sizing: border-box;
    width: 1200px;
    height: 680px;
    background: var(--card-bg);
    border: 2px solid var(--card-border);
    font-family: "Arimo", Arial, sans-serif;
    color: var(--text-peach);
  }
  .brand-mark {
    position: absolute;
    left: 70px;
    top: 110px;
    width: 120px;
    height: 120px;
    border-radius: 50%;
    background: var(--mark-pink);
  }
  .brand-name {
    position: absolute;
    left: 52px;
    top: 262px;
    margin: 0;
    font-size: 25px;
    font-weight: 400;
    color: var(--mark-pink);
    line-height: 1.25;
  }
  .hours-tagline {
    position: absolute;
    left: 236px;
    top: 118px;
    margin: 0;
    font-family: "Italianno", cursive;
    font-size: 76px;
    font-weight: 400;
    line-height: 1;
    color: var(--script-mauve);
    white-space: nowrap;
  }
  .person {
    position: absolute;
    left: 0;
    right: 0;
    top: 288px;
    text-align: center;
    padding-left: 82px;
  }
  .person-name {
    margin: 0;
    font-size: 38px;
    font-weight: 700;
    line-height: 1.15;
  }
  .person-title {
    margin: 0;
    font-size: 35px;
    font-weight: 400;
    line-height: 1.2;
  }
  .contact-list,
  .address {
    position: absolute;
    top: 460px;
    margin: 0;
    padding: 0;
    list-style: none;
    font-size: 36px;
    line-height: 46px;
    font-style: normal;
    white-space: nowrap;
  }
  .contact-list { left: 52px; }
  .address {
    right: 33px;
    text-align: right;
  }
</style>
</head>
<body>
  <div class="card">
    <div class="brand-mark" aria-hidden="true"></div>
    <p class="brand-name">Willowmere Spa<br>and Beauty</p>

    <p class="hours-tagline">Open 7days per week from 8am to 8pm</p>

    <div class="person">
      <h1 class="person-name">Marissa Thornbury</h1>
      <p class="person-title">Spa Facilitator</p>
    </div>

    <ul class="contact-list">
      <li>OFFICE: 416.739.4100</li>
      <li>FAX: 416.739.4101</li>
      <li>CELL: 416.582.6074</li>
      <li>EMAIL: marissa.thornbury@willowmerespa.example</li>
    </ul>

    <address class="address">
      Willowmere Spa and Beauty Ltd.<br>
      7200 Calder Ave; Suite 1400<br>
      Toronto ON K8P 2W7
    </address>
  </div>
</body>
</html>
```